Connected Building Infrastructure Business needs awesome document templates.

We'd like to have a fresh set of document templates for business letters, documents, and power point presentations. Brindlewood Wiring and Safety works with IT teams, construction firms, and consultants to provide structured cabling, electronic security, and connected building infrastructure services to firms through the state of New York, Massachusetts, and Vermont.

We have recently refreshed our logo and have started some branding and would like to continue the themes already in place. As a result of this project we are looking for

-letter head template
-document template for sales material (contracts and proposals)
-document template for customer documentation and hand outs
-PowerPoint template for customer and internal presentations

Target Market(s)

CIOs, Vice President of IT Facilities, and Security, Small/Medium Size Business Owners, General Contractors

Industry/Entity Type

Business

Font styles to use
Sans Serif

Requirements
Must have
• -letter head template
• -document template for sales material (contracts and proposals)
• -document template for customer documentation and hand outs
• -PowerPoint template for customer and internal presentations
Should not have
• Do not change logo. Can use knockout and/or black and white version of logo if needed.

```html
<!DOCTYPE html>
<html lang="en">
<head>
<meta charset="utf-8">
<title>Brindlewood Wiring and Safety – Document Templates</title>
<link rel="stylesheet" href="https://fonts.googleapis.com/css2?family=Montserrat:wght@300;400;500;700;800;900&display=swap">
<style>
  :root{
    --green:#0b6b3a;
    --green-dark:#064d2a;
    --green-soft:#4f9474;
    --ink:#1d1d1d;
    --paper:#f3f3f3;
    --board:#e6e6e6;
    --frame:#f5f5f5;
    --grey:#7a7a7a;
    --white:#ffffff;
  }
  *{box-sizing:border-box;margin:0;padding:0}
  html,body{width:1196px;height:1200px;overflow:hidden;background:var(--frame);font-family:"Montserrat",sans-serif;color:var(--ink)}
  .board{position:absolute;left:22px;top:16px;width:1150px;height:1154px;background:var(--board)}
  .sheet{position:absolute;background:var(--paper);overflow:hidden;box-shadow:0 10px 10px -6px rgba(0,0,0,.35)}

  /* Decorative bands: flat fills standing in for the wave artwork */
  .band{position:absolute;left:0;right:0}
  .band-top{top:0;height:14px;background:linear-gradient(90deg,var(--ink) 0%,var(--ink) 45%,var(--green) 100%);border-bottom:3px solid var(--green)}
  .band-foot-ink{bottom:0;background:var(--ink);border-top:4px solid var(--green)}
  .band-foot-green{bottom:0;background:linear-gradient(90deg,var(--green-dark),var(--green));border-top:12px solid var(--ink)}
  .band-foot-soft{bottom:0;background:linear-gradient(90deg,var(--green-soft),#5f8a72);border-top:6px solid var(--grey)}

  .brand{position:absolute;font-weight:800;color:var(--ink);line-height:1;letter-spacing:.02em}
  .brand .mark{display:inline-block;background:var(--green);vertical-align:middle}
  .brand .tag{display:block;font-size:.48em;letter-spacing:.04em;margin-top:2px}
  .brand .url{display:block;font-weight:800;font-size:.42em;margin-top:2px;letter-spacing:0}

  .contact{color:var(--white);text-align:right}
  .contact .row{display:flex;justify-content:flex-end;align-items:center;gap:5px}
  .contact svg{flex:none}

  /* Letterhead */
  .letterhead{left:167px;top:103px;width:380px;height:539px}
  .letterhead .body{position:absolute;left:43px;top:164px;width:282px;font-size:10.3px;line-height:13.2px}
  .letterhead .body p{margin-bottom:9px}
  .letterhead .signature{position:absolute;left:45px;top:468px;font-size:9.5px;font-weight:700}
  .letterhead .contact{position:absolute;right:16px;top:494px;font-size:5.8px;line-height:7px}

  /* Proposal cover */
  .proposal{left:602px;top:101px;width:427px;height:552px}
  .proposal .title{position:absolute;left:50px;top:153px;font-weight:900;font-size:43px;line-height:38px;letter-spacing:.01em}
  .proposal .title-rule{position:absolute;left:52px;top:235px;width:245px;height:2px;background:var(--ink)}
  .proposal .services{position:absolute;left:54px;top:253px;list-style:none;font-size:14px;line-height:21.4px;letter-spacing:.02em}
  .proposal .contact{position:absolute;right:40px;top:452px;font-size:9px;line-height:10.5px}
  .proposal .contact .row{margin-bottom:6px}

  /* Slides */
  .slide{top:736px;width:395px;height:295px}
  .slide-title{left:158px}
  .slide-text{left:613px}
  .slide-title .heading{position:absolute;left:50px;top:122px;font-size:17.8px;font-weight:500;letter-spacing:.03em}
  .slide-title .heading-rule{position:absolute;left:50px;top:148px;width:309px;height:1px;background:var(--ink)}
  .slide-title .sub{position:absolute;right:39px;top:153px;text-align:right;font-size:13px;font-weight:300;line-height:20px}
  .slide-text .body{position:absolute;left:36px;right:36px;top:108px;text-align:center;font-size:12.6px;line-height:15.6px}
</style>
</head>
<body>
<div class="board">

  <!-- Letterhead -->
  <section class="sheet letterhead">
    <div class="band band-top" role="img" aria-label="Decorative header band in black and green"></div>
    <div class="band band-foot-ink" style="height:56px" role="img" aria-label="Decorative footer band in black and green"></div>
    <div class="brand" style="right:18px;top:24px;font-size:8px"><span class="mark" style="width:7px;height:7px;margin-right:3px"></span>BRINDLEWOOD<span class="tag">WIRING AND SAFETY</span><span class="url">www.brindlewoodwiring.com</span></div>
    <div class="brand" style="left:46px;top:96px;font-size:11px">BRINDLEWOOD<span class="tag">WIRING AND SAFETY</span></div>
    <div class="body">
      <p>Brindlewood Wiring and Safety is the premier provider ofnetwork cabling and integrated security systems in the capitaldistrict. We work with IT teams, architects, building owners,and technology consultants to provide first class structured cabling and electronic security solutions.</p>
      <p>Brindlewood Wiring and Safety is the premier provider ofnetwork cabling and integrated security systems in the capitaldistrict. We work with IT teams, architects, building owners,and technology consultants to provide first class structured cabling and electronic security solutions.</p>
      <p>Brindlewood Wiring and Safety is the premier provider ofnetwork cabling and integrated security systems in the capitaldistrict. We work with IT teams, architects, building owners,and technology consultants to provide first class structured cabling and electronic security solutions.</p>
    </div>
    <div class="signature">SIGNATURE</div>
    <div class="contact">
      <div class="row"><span>(555) 301-0187</span><svg width="7" height="7" viewBox="0 0 10 10"><path d="M2 1l2 2-1 1.5c.8 1.4 1.6 2.2 3 3L7.5 6l2 2-1.5 1.5C5 9 1 5 .5 1.5Z" fill="var(--white)"/></svg></div>
      <div class="row"><span>Brindlewood Wiring and Safety<br>42 Larkfield Rd.<br>Troy, NY 12180</span><svg width="7" height="9" viewBox="0 0 10 13"><path d="M5 0a5 5 0 0 1 5 5c0 3-5 8-5 8S0 8 0 5a5 5 0 0 1 5-5Z" fill="var(--white)"/><circle cx="5" cy="5" r="2" fill="var(--ink)"/></svg></div>
      <div class="row"><span>info@brindlewoodwiring.com</span><svg width="9" height="6" viewBox="0 0 12 8"><rect x=".5" y=".5" width="11" height="7" fill="none" stroke="var(--white)"/><path d="M.5 .5 6 5l5.5-4.5" fill="none" stroke="var(--white)"/></svg></div>
    </div>
  </section>

  <!-- Proposal cover -->
  <section class="sheet proposal">
    <div class="band band-top" role="img" aria-label="Decorative header band in black and green"></div>
    <div class="band band-foot-green" style="height:122px" role="img" aria-label="Decorative footer band in black and green"></div>
    <div class="brand" style="right:20px;top:24px;font-size:8px"><span class="mark" style="width:7px;height:7px;margin-right:3px"></span>BRINDLEWOOD<span class="tag">WIRING AND SAFETY</span><span class="url">www.brindlewoodwiring.com</span></div>
    <div class="brand" style="left:76px;top:96px;font-size:11px">BRINDLEWOOD<span class="tag">WIRING AND SAFETY</span></div>
    <h1 class="title">PRODUCT<br>PROPOSAL</h1>
    <div class="title-rule"></div>
    <ul class="services">
      <li>Structured Cabling</li>
      <li>Fire Detection</li>
      <li>Security and Surveillance</li>
      <li>Audio/Video</li>
      <li>In-Building Wireless</li>
      <li>24/7 x 365 Monitoring</li>
    </ul>
    <div class="contact">
      <div class="row"><span>(555) 301-0187</span><svg width="11" height="11" viewBox="0 0 10 10"><path d="M2 1l2 2-1 1.5c.8 1.4 1.6 2.2 3 3L7.5 6l2 2-1.5 1.5C5 9 1 5 .5 1.5Z" fill="var(--white)"/></svg></div>
      <div class="row"><span>info@brindlewoodwiring.com</span><svg width="13" height="9" viewBox="0 0 12 8"><rect x=".5" y=".5" width="11" height="7" fill="none" stroke="var(--white)"/><path d="M.5 .5 6 5l5.5-4.5" fill="none" stroke="var(--white)"/></svg></div>
      <div class="row"><span>Brindlewood Wiring and Safety<br>42 Larkfield Rd.<br>Troy, NY 12180</span><svg width="11" height="14" viewBox="0 0 10 13"><path d="M5 0a5 5 0 0 1 5 5c0 3-5 8-5 8S0 8 0 5a5 5 0 0 1 5-5Z" fill="var(--white)"/><circle cx="5" cy="5" r="2" fill="var(--green)"/></svg></div>
    </div>
  </section>

  <!-- Presentation title slide -->
  <section class="sheet slide slide-title">
    <div class="band band-top" role="img" aria-label="Decorative header band in black and green"></div>
    <div class="band band-foot-soft" style="height:52px" role="img" aria-label="Decorative footer band in soft green and grey"></div>
    <div class="brand" style="left:12px;top:24px;font-size:9px"><span class="mark" style="width:8px;height:8px;margin-right:4px"></span>BRINDLEWOOD<span class="tag" style="margin-left:12px">WIRING AND SAFETY</span></div>
    <h2 class="heading">BRINDLEWOOD PRESENTATION</h2>
    <div class="heading-rule"></div>
    <div class="sub">Marketing Of BRINDLEWOOD<br>12th December 216</div>
  </section>

  <!-- Presentation content slide -->
  <section class="sheet slide slide-text">
    <div class="band band-top" role="img" aria-label="Decorative header band in black and green"></div>
    <div class="brand" style="left:12px;top:24px;font-size:9px"><span class="mark" style="width:8px;height:8px;margin-right:4px"></span>BRINDLEWOOD<span class="tag" style="margin-left:12px">WIRING AND SAFETY</span></div>
    <p class="body">Brindlewood Wiring and Safety is the premier provider ofnetwork cabling and integrated security systems in the capitaldistrict. We work with IT teams, architects, building owners,and technology consultants to provide first class structured cabling and electronic security solutions.</p>
  </section>

</div>
</body>
</html>
```